Criação de Layout para Website para alimenticio
" A Ve Brinola é uma empresa que produz doces finos para eventos (corporativos e sociais), cujo público alvo são consumidores que valorizam um produto de qualidade e diferenciado. "

```html
<!DOCTYPE html>
<html lang="pt-BR">
<head>
<meta charset="utf-8">
<title>Ve Brinola — Doces finos para eventos</title>
<link href="https://fonts.googleapis.com/css2?family=Open+Sans:wght@400;600;700&display=swap" rel="stylesheet">
<style>
:root{
  --brown:#5b4e43;
  --brown-dark:#4a3f36;
  --aqua:#c9ebee;
  --aqua-deep:#b8e2e6;
  --panel:#f8f8f8;
  --line:#e2e2e2;
  --white:#ffffff;
  --muted:#8a8a8a;
}
*{margin:0;padding:0;box-sizing:border-box}
html,body{width:1159px;height:1200px;overflow:hidden;background:var(--white);font-family:"Open Sans",sans-serif;color:var(--brown)}
.page{position:relative;width:1159px;height:1200px}
.abs{position:absolute}

.social{top:90px;left:935px;display:flex;gap:6px}
.social span{width:36px;height:36px;border-radius:50%;background:var(--brown-dark);display:block}
.search{top:136px;left:844px;width:251px;height:24px;background:#e6e6e6;display:flex;justify-content:flex-end}
.search-btn{width:28px;height:24px;background:var(--brown);display:flex;align-items:center;justify-content:center}

.main-panel{top:216px;left:60px;width:1038px;height:778px;background:var(--panel);border:1px solid var(--line);border-top:none}
.nav{top:173px;left:60px;width:1038px;height:44px;background:var(--brown);color:var(--white);font-size:17px}
.nav .item{position:absolute;top:0;height:44px;line-height:44px;text-align:center;border-left:1px solid rgba(0,0,0,.18)}
.burger{position:absolute;left:21px;top:12px;width:24px}
.burger i{display:block;height:3px;background:var(--white);margin-bottom:5px}

.brand{top:55px;left:458px;width:250px;height:250px;border-radius:50%;background:var(--aqua);border:4px solid var(--brown);display:flex;align-items:center;justify-content:center}
.brand span{font-size:40px;font-weight:700;color:var(--brown);letter-spacing:-.5px}

.thumb{left:70px;width:316px;height:80px}
.hero{top:254px;left:395px;width:692px;height:432px;background:linear-gradient(180deg,#c9a45a 0%,#7a3a1f 40%,#5a3a22 70%,#8b7a5e 100%)}
.hero-overlay{top:217px;left:0;width:692px;height:158px;background:rgba(30,22,16,.72);color:var(--white);padding:8px 17px}
.hero-overlay h1{font-weight:400;font-size:29px;line-height:1.2;letter-spacing:-.3px}
.hero-overlay p{font-size:14px;line-height:23px;margin-top:12px;color:#eee}
.hero-btns{margin-top:8px;display:flex;gap:10px}
.btn-solid{background:var(--aqua);color:var(--brown);font-weight:600;font-size:13px;padding:0 11px;height:34px;line-height:34px}
.btn-ghost{border:1.5px solid var(--white);color:var(--white);font-weight:600;font-size:13px;padding:0 10px;height:34px;line-height:31px}
.dots{position:absolute;right:16px;bottom:12px;display:flex;gap:7px}
.dots i{width:9px;height:9px;border-radius:50%;border:1.5px solid var(--white)}
.dots i.on{background:var(--white)}

.section-title{font-size:26px;font-weight:700;letter-spacing:.5px;text-align:center}
.card{top:753px;width:203px;height:232px}
.card .img{height:175px}
.card .cap{height:57px;background:var(--aqua);padding:10px 15px}
.card h3{font-size:15px;font-weight:700;letter-spacing:.2px}
.card p{font-size:10.5px;color:var(--muted);margin-top:2px}

.tabs{top:751px;left:815px;width:268px;height:36px;display:flex;font-size:13px}
.tabs div{flex:1;text-align:center;line-height:36px}
.tab-on{background:var(--aqua);color:var(--brown-dark)}
.tab-off{background:var(--brown);color:var(--white)}
.read{left:815px;width:268px;height:89px;background:var(--aqua);display:flex}
.read .img{width:90px;height:89px}
.read a{font-size:13px;color:var(--brown);line-height:18px;padding:0 10px 0 12px;align-self:center;text-decoration:underline}

.rule{top:1022px;left:62px;width:1023px;height:1px;background:#bdb6b0}
.foot h2{font-size:31px;font-weight:400;color:var(--brown)}
.foot p{font-size:13px;line-height:16px;color:var(--brown-dark)}
.small-btn{background:var(--aqua);color:var(--brown-dark);font-size:12.5px;text-align:center;line-height:23px;height:23px}
</style>
</head>
<body>
<div class="page">

  <div class="abs social" aria-label="Redes sociais"><span></span><span></span><span></span><span></span></div>
  <div class="abs search">
    <div class="search-btn"><svg width="12" height="12" viewBox="0 0 12 12"><circle cx="5" cy="5" r="3.4" fill="none" stroke="#fff" stroke-width="1.6"/><line x1="7.5" y1="7.5" x2="11" y2="11" stroke="#fff" stroke-width="2"/></svg></div>
  </div>

  <div class="abs main-panel"></div>

  <nav class="abs nav">
    <div class="burger"><i></i><i></i><i></i></div>
    <div class="item" style="left:71px;width:160px;border-left:none">HOME</div>
    <div class="item" style="left:171px;width:0"></div>
    <div class="item" style="left:171px;width:150px">QUEM SOMOS</div>
    <div class="item" style="left:322px;width:70px"></div>
    <div class="item" style="left:774px;width:139px">PRODUTOS</div>
    <div class="item" style="left:913px;width:125px">CONTATO</div>
  </nav>

  <div class="abs thumb" style="top:254px;background:linear-gradient(90deg,#6d3a1f,#a8703e,#e8e0cf,#8a4a25,#6d3a1f)" role="img" aria-label="Mesa de doces com bolo de casamento"></div>
  <div class="abs thumb" style="top:340px;background:linear-gradient(90deg,#d8c49c,#f1eadb,#b8833f,#eee4d0)" role="img" aria-label="Doces finos embalados em tecido"></div>
  <div class="abs thumb" style="top:428px;background:linear-gradient(90deg,#6d3a1f,#a8703e,#e8e0cf,#8a4a25,#6d3a1f)" role="img" aria-label="Mesa de doces com bolo de casamento"></div>
  <div class="abs thumb" style="top:515px;background:linear-gradient(90deg,#2a241c,#d9a33a,#e6b84a,#c08a2a)" role="img" aria-label="Copinhos de doce de maracujá"></div>
  <div class="abs thumb" style="top:605px;background:linear-gradient(90deg,#6d3a1f,#a8703e,#e8e0cf,#8a4a25,#6d3a1f)" role="img" aria-label="Mesa de doces com bolo de casamento"></div>

  <div class="abs hero" role="img" aria-label="Salão decorado com mesa de doces para evento">
    <div class="abs hero-overlay">
      <h1>SEJA BEM VINDO !</h1>
      <p>A <b>Ve Brinola</b> é uma empresa que produz doces finos para eventos (corporativos e sociais).<br>Conheça nos melhor clicando no botão Tour, ou saiba mais sobre nossos serviços</p>
      <div class="hero-btns"><span class="btn-solid">SAIBA MAIS</span><span class="btn-ghost">VÍDEO TOUR</span></div>
      <div class="dots"><i></i><i class="on"></i><i></i></div>
    </div>
  </div>

  <div class="abs brand"><span>Ve Brinola</span></div>

  <h2 class="abs section-title" style="top:708px;left:272px;width:200px">CONFIRA:</h2>

  <div class="abs card" style="left:68px">
    <div class="img" style="background:linear-gradient(135deg,#f2d36b,#e8508a,#f4ecdf,#8cc66a,#e0407c)" role="img" aria-label="Macarons coloridos"></div>
    <div class="cap"><h3>NOSSOS PRODUTOS</h3><p>Conheça nossa linhda de produtos.</p></div>
  </div>
  <div class="abs card" style="left:280px">
    <div class="img" style="background:linear-gradient(135deg,#c98a2a,#f0b53a,#e9c56a,#b87a22)" role="img" aria-label="Doces em copinhos com laço"></div>
    <div class="cap"><h3>RECEITAS</h3><p>Venha compartilhar receitas.</p></div>
  </div>
  <div class="abs card" style="left:495px">
    <div class="img" style="background:linear-gradient(135deg,#9a9a96,#f1ece2,#cfc8ba,#7d7b76)" role="img" aria-label="Doces em forma de concha com pérolas"></div>
    <div class="cap"><h3>DOCES P/ SEU EVENTO</h3><p>Confira nossas alternativas</p></div>
  </div>

  <h2 class="abs section-title" style="top:708px;left:815px;width:262px">ÚLTIMAS LIDAS</h2>
  <div class="abs tabs"><div class="tab-on">MAIS VISITADOS</div><div class="tab-off">NOVIDADES</div></div>
  <div class="abs read" style="top:798px">
    <div class="img" style="background:linear-gradient(135deg,#9a9a96,#f1ece2,#cfc8ba)" role="img" aria-label="Doces em forma de concha"></div>
    <a>Faça conosco seu evento, seja ele social ou corpo-rativo.</a>
  </div>
  <div class="abs read" style="top:897px">
    <div class="img" style="background:linear-gradient(135deg,#e0407c,#f4ecdf,#8cc66a,#e8508a)" role="img" aria-label="Macarons coloridos"></div>
    <a>Confira nossa lista de doces</a>
  </div>

  <div class="abs rule"></div>

  <div class="abs foot" style="top:1036px;left:114px">
    <h2>Atendimento</h2>
    <p>Fone: (011) 4870-2165<br>ola@vebrinola.com.br</p>
  </div>
  <div class="abs foot" style="top:1036px;left:358px">
    <h2>Onde Estamos</h2>
    <p>Rua das Acácias, 287 - 3º andar -<br>Sala 12 São Paulo – SP<br>CEP 04320-110</p>
  </div>
  <div class="abs foot" style="top:1036px;left:622px">
    <h2>Orçamento</h2>
    <p>Solicite um orçamento<br>sem compromisso.</p>
  </div>
  <div class="abs small-btn" style="top:1114px;left:624px;width:91px">SOLICITAR</div>
  <div class="abs foot" style="top:1038px;left:827px">
    <h2>Newslatter</h2>
    <p style="margin-top:1px">Receba nossas novidades</p>
  </div>
  <svg class="abs" style="top:1098px;left:828px" width="18" height="16" viewBox="0 0 18 16"><path d="M1 7 L9 1 L17 7 V15 H1 Z" fill="none" stroke="#4a3f36" stroke-width="1.8"/><path d="M1 7 L9 12 L17 7" fill="none" stroke="#4a3f36" stroke-width="1.8"/></svg>
  <div class="abs" style="top:1095px;left:851px;width:159px;height:22px;background:#eaeaea"></div>
  <div class="abs small-btn" style="top:1124px;left:918px;width:91px">CADASTRAR</div>

</div>
</body>
</html>
```